Brightwave Audiology Letterhead redesign project

We need a full redesign of our current letterhead to make it consistent with the look and feel of our website design www.brightwaveaudio.com.au. It will need to include all information on the current version attached. The letterhead is used for sending medical reports and general correspondence. It should make use of our corporate colours (purple and teal) as per the logo on the existing file. The letterhead should be bold and eye-catching.

Target Market(s)

Medical practitioners.

Font styles to use
Sans Serif

Requirements
Must have
• It will need to include all information on the current version. Must have a premium, professional, high-end look and feel.
Nice to have
• Bold and eye-catching letterhead that reinforces the Brightwave Audiology brand. To stand out from other traditional letterheads.
Should not have
• The design should not be too cluttered or 'busy'

```html
<!DOCTYPE html>
<html lang="en">
<head>
<meta charset="utf-8">
<title>Brightwave Audiology — Letterhead</title>
<link rel="stylesheet" href="https://fonts.googleapis.com/css2?family=Nunito:wght@900&family=Open+Sans:wght@400&display=swap">
<style>
  :root {
    --brand-purple: #6f3a8c;
    --paper: #ffffff;
    --ink: #231f20;
    --backdrop: #e9e6e1;
    --canvas-w: 1198px;
    --canvas-h: 1200px;
  }
  * { box-sizing: border-box; margin: 0; padding: 0; }
  html, body {
    width: var(--canvas-w);
    height: var(--canvas-h);
    overflow: hidden;
    background: var(--backdrop);
  }
  .canvas {
    position: relative;
    width: var(--canvas-w);
    height: var(--canvas-h);
  }
  .letterhead {
    position: absolute;
    left: 161px;
    top: 31px;
    width: 868px;
    height: 1125px;
    background: var(--paper);
    box-shadow: 0 2px 10px rgba(0, 0, 0, 0.12);
    overflow: hidden;
  }
  .brand-panel {
    position: absolute;
    left: 0;
    top: 0;
    width: 338px;
    height: 231px;
    background: var(--brand-purple);
    border-bottom-right-radius: 58% 62%;
  }
  .brand-name {
    position: absolute;
    left: 30px;
    top: 56px;
    width: 260px;
    font-family: "Nunito", sans-serif;
    font-weight: 900;
    font-size: 44px;
    line-height: 46px;
    letter-spacing: -0.5px;
    color: var(--paper);
  }
  .contact-block {
    position: absolute;
    right: 30px;
    top: 30px;
    text-align: right;
    font-family: "Open Sans", sans-serif;
    font-style: normal;
    font-weight: 400;
    font-size: 11.5px;
    line-height: 15.5px;
    color: var(--ink);
  }
  .contact-block .label { color: var(--brand-purple); }
</style>
</head>
<body>
  <main class="canvas">
    <article class="letterhead">
      <header class="brand-panel">
        <div class="brand-name">Brightwave Audiology</div>
      </header>
      <address class="contact-block">
        <div><span class="label">CLINIC</span> 48 Carrow Street, Kelmont, Qld 4352</div>
        <div><span class="label">TEL</span> 07 4610 2284 <span class="label">FAX</span> 07 4610 2285</div>
        <div><span class="label">EMAIL</span> care@brightwaveaudio.com.au</div>
        <div>www.brightwaveaudio.com.au</div>
      </address>
    </article>
  </main>
</body>
</html>
```